~~ Night Club Website ~~

We would like to redo our website for Ember Velvet Hall (http://www.embervelvethall.example).

Ember Velvet Hall is Edmonton's #1 electronic dance music night club.

We have DJs that fly in from around the world to play at our club and want to be able to properly showcase our upcoming shows and events to increase sales.

I have now guaranteed the project.  Let's see some brilliant designs!

Target Market(s)

Electronic Dance Music Lovers; College / University Students; Young Professionals

Industry/Entity Type

Electronic

Requirements
Must have
• The site must have the following sections:

1. Home Page
- Rotating Banner where we can put upcoming events
- Twitter, Circlebook, YouTube, FourSquare buttons
- Our Twitter feed to automatically post
- Circlebook integration with 'Like' and Comments for upcoming shows
- An email signup section for contests and giveaways that auto-updates the email list in MailChimp
- Streaming music from 7 Pulse Radio

2. Photos
- This needs to integrate right into our Circlebook Albums

3. Weekly Lineup

4. Events
- People need to be able to buy tickets right online via SwiftPay

5. Bookings
- People need to be able to pick a party package and pay right online via SwiftPay

6. Contact Us

```html
<!DOCTYPE html>
<html lang="en">
<head>
<meta charset="utf-8">
<title>Ember Velvet Hall</title>
<link href="https://fonts.googleapis.com/css2?family=Days+One&family=Ubuntu:wght@400;500;700&display=swap" rel="stylesheet">
<style>
:root{
  --bg:#07070a;
  --panel:#050506;
  --panel-line:#3a3a3e;
  --orange:#e27a1c;
  --orange-light:#f3a044;
  --silver:#c9ccd2;
  --text:#f2f2f2;
  --muted:#bdbdbd;
  --field:#232326;
  --tab:#2a2a2d;
}
*{box-sizing:border-box;margin:0;padding:0}
html,body{width:1065px;height:1200px;overflow:hidden}
body{
  position:relative;
  font-family:"Ubuntu",sans-serif;color:var(--text);
  background:
    radial-gradient(ellipse 600px 160px at 530px 40px, rgba(196,96,20,.55), transparent 70%),
    linear-gradient(180deg,#1a0f08 0,#09090c 200px,#0b0c10 780px,#121419 1050px,#08080a 1200px);
}
.abs{position:absolute}
.logo{left:107px;top:7px;width:110px;height:142px;background:#000;border:1px solid #222;
  display:flex;flex-direction:column;align-items:center;justify-content:center;gap:8px}
.logo-mark{width:40px;height:40px;border:3px solid #6fd6e6}
.logo-name{font-size:12px;font-weight:500;color:#6fd6e6;text-align:center;line-height:1.3;letter-spacing:1px}
.social{left:829px;top:20px;display:flex;gap:10px}
.social span{width:26px;height:26px;border-radius:4px;display:block}
.nav{left:217px;top:62px;width:759px;height:43px;border-radius:0 22px 22px 0;
  background:linear-gradient(#3b3b3f,#0e0e10);border:2px solid #555;border-left:none}
.nav-home{left:255px;top:52px;width:63px;height:61px;border-radius:0 0 8px 8px;
  background:linear-gradient(#f09a3a,#d46a12);color:#fff;font-size:12px;font-weight:500;
  display:flex;align-items:center;justify-content:center}
.nav-item{top:62px;height:43px;display:flex;align-items:center;font-size:12px;color:#d8d8d8;transform:translateX(-50%)}
.nav-sep{top:66px;width:1px;height:35px;background:#111;box-shadow:1px 0 0 #444}
.hero{left:107px;top:164px;width:869px;height:337px;border-radius:16px;border:2px solid #3a3a3e;overflow:hidden;
  background:linear-gradient(90deg,#0b0806 0,#150b05 45%,#2a1608 70%)}
.hero-art{position:absolute;right:0;top:0;width:440px;height:100%;
  background:radial-gradient(circle at 40% 30%,#b44b6a,transparent 55%),radial-gradient(circle at 80% 70%,#3a5fb0,transparent 60%),linear-gradient(90deg,rgba(40,20,10,0),#6a3a24 40%,#2c1c2a)}
.hero-title{position:absolute;left:33px;top:24px;font-family:"Days One",sans-serif;font-size:42px;line-height:58px}
.hero-title .a{color:#a9c8d8}
.hero-title .b{color:var(--orange)}
.hero-sub{position:absolute;left:21px;top:148px;font-size:13px;font-weight:500}
.hero-text{position:absolute;left:21px;top:178px;width:420px;font-size:11.5px;line-height:16px;color:#e8e8e8}
.btn-events{position:absolute;left:26px;top:262px;width:130px;height:38px;border-radius:20px;
  background:linear-gradient(#f0962e,#c85e0e);border:2px solid #7a3a08;box-shadow:0 0 0 2px #f2a14a inset;
  color:#fff;font-size:19px;display:flex;align-items:center;justify-content:center}
.welcome{left:107px;top:532px;width:530px}
h2{font-family:"Days One",sans-serif;font-size:21px;font-weight:400;color:var(--silver);letter-spacing:.5px}
h2 em{font-style:normal;color:var(--orange)}
.welcome .lead{margin-top:14px;color:var(--orange);font-size:12.5px;font-weight:500;letter-spacing:.3px}
.welcome p{margin-top:16px;font-size:12.5px;line-height:16px;letter-spacing:.2px}
.panel{background:var(--panel);border:1px solid var(--panel-line);border-radius:12px}
.gallery{left:658px;top:530px;width:317px;height:220px;padding:10px 20px}
.gallery .caption{font-size:10.5px;margin-top:12px}
.thumbs{display:grid;grid-template-columns:repeat(3,89px);gap:16px 13px;margin-top:15px;margin-left:-7px}
.thumbs span{height:51px;border:1px solid #888;display:block}
.arrows{position:absolute;right:12px;bottom:7px;font-size:13px;color:#aaa;letter-spacing:4px}
.box{top:771px;height:254px}
.box-head{margin:9px 10px 0;height:34px;border-radius:6px;background:var(--tab);
  font-family:"Days One",sans-serif;font-size:20px;display:flex;align-items:center;justify-content:center}
.social-box{left:104px;width:251px}
.social-box .box-head{color:#1f8ad6}
.social-box .page{margin:14px 0 0 18px;color:var(--orange);font-size:11px;font-weight:500}
.fans{display:grid;grid-template-columns:repeat(4,47px);gap:9px 12px;margin:16px 0 0 14px}
.fans span{height:47px;border:1px solid #444;display:block}
.like{position:absolute;left:15px;top:203px;width:49px;height:21px;background:#f3f3f3;border:1px solid #aaa;border-radius:3px}
.like-info{position:absolute;left:80px;top:199px;font-size:11px;line-height:16px}
.booking{left:378px;width:251px}
.booking .box-head{color:var(--silver)}
.booking .box-head em{font-style:normal;color:var(--orange)}
.item{position:absolute;left:15px;width:225px;height:80px}
.item .pic{position:absolute;left:0;top:0;width:80px;height:68px;border:2px solid #ccc}
.item .name{position:absolute;left:99px;top:3px;font-size:11.5px;color:#ddd}
.item .price{position:absolute;left:103px;top:20px;font-family:"Days One",sans-serif;font-size:20px;color:var(--orange)}
.item .info,.item .buy{position:absolute;top:61px;height:17px;font-size:10px;font-weight:700;display:flex;align-items:center;justify-content:center}
.item .info{left:109px;width:54px;background:linear-gradient(#fff,#bbb);color:#333}
.item .buy{left:172px;width:54px;background:#e0561a;color:#fff}
.signup{left:658px;width:317px}
.signup h2{position:absolute;left:15px;top:7px}
.field{position:absolute;left:14px;width:167px;height:23px;border-radius:6px;background:var(--field);border:1px solid #444;
  font-size:11px;color:#bbb;padding:4px 12px}
.poster{position:absolute;right:2px;top:44px;width:118px;height:190px}
.btn-sign{position:absolute;left:19px;top:206px;width:73px;height:30px;border-radius:16px;
  background:linear-gradient(#f0962e,#c85e0e);border:2px solid #7a3a08;box-shadow:0 0 0 2px #f2a14a inset;
  font-family:"Days One",sans-serif;font-size:13px;color:#fff;display:flex;align-items:center;justify-content:center}
.footer{left:89px;top:1079px;width:885px;height:87px;border-radius:12px;border:1px solid var(--panel-line);background:rgba(5,5,6,.9)}
.footer nav{position:absolute;left:10px;top:13px;font-size:11.5px;font-weight:500;display:flex;gap:15px}
.footer nav i{font-style:normal;color:#ccc}
.footer .legal{position:absolute;left:10px;top:36px;font-size:11.5px;line-height:21px}
.pay{position:absolute;right:20px;top:10px;width:140px;text-align:center}
.pay small{font-size:8px;display:block}
.pay b{font-size:18px;color:#2f7fd0;display:block;margin-top:2px}
.cards{display:flex;gap:6px;justify-content:center;margin-top:6px}
.cards span{width:27px;height:16px;border-radius:2px;background:#e6e6e6;display:block}
</style>
</head>
<body>
  <div class="abs logo"><span class="logo-mark"></span><span class="logo-name">EMBER<br>VELVET HALL</span></div>

  <div class="abs social" aria-label="Social links">
    <span style="background:#5aa6d8"></span><span style="background:#3b5a98"></span><span style="background:#3fb3e4"></span><span style="background:#d02b25"></span>
  </div>

  <div class="abs nav"></div>
  <div class="abs nav-home">HOME</div>
  <div class="abs nav-sep" style="left:341px"></div>
  <div class="abs nav-item" style="left:388px">PHOTO</div>
  <div class="abs nav-sep" style="left:435px"></div>
  <div class="abs nav-item" style="left:514px">WEEKLY SPECIALS</div>
  <div class="abs nav-sep" style="left:602px"></div>
  <div class="abs nav-item" style="left:651px">EVENTS</div>
  <div class="abs nav-sep" style="left:711px"></div>
  <div class="abs nav-item" style="left:771px">BOOKING</div>
  <div class="abs nav-sep" style="left:836px"></div>
  <div class="abs nav-item" style="left:909px">CONTACT US</div>

  <section class="abs hero">
    <div class="hero-art" role="img" aria-label="Illustration of a DJ with headphones in front of colourful club lights"></div>
    <div class="hero-title"><div class="a">EMBER</div><div class="b">VELVET HALL</div></div>
    <div class="hero-sub">Ember Velvet Hall - Maple Avenue’s Premium Bottle Service Lounge</div>
    <div class="hero-text">Enjoy friendly service from when you first arrive at the door and throughout your night from our bartenders and servers.Our collection of well known Resident DJ’s will be spinning your favorite tracks and guiding your musical entertainment in House, Dirty Electro, and funky Mashups</div>
    <div class="btn-events">Get Events</div>
  </section>

  <section class="abs welcome">
    <h2>Welcome <em>Velvet Hall</em></h2>
    <div class="lead">Ember Velvet Hall - Maple Avenue’s Premium Bottle Service Lounge</div>
    <p>Enjoy friendly service from when you first arrive at the door and throughout your night from our bartenders and servers.</p>
    <p>Our collection of well known Resident DJ’s will be spinning your favorite tracks and guiding your musical entertainment in House, Dirty Electro, and funky Mashups</p>
    <p>Dress to impress and relax with friends in one of our VIP booths and receive personalized bottle service - Please call ahead to make reservations</p>
  </section>

  <section class="abs panel gallery">
    <h2>Latest <em>Gallery</em></h2>
    <div class="caption">Nova Lane performs " Midnight Glow" by Ruby Hart.</div>
    <div class="thumbs">
      <span role="img" aria-label="Singer performing on stage" style="background:linear-gradient(135deg,#c23a8a,#3a6ab0)"></span>
      <span role="img" aria-label="Performers seated on stage" style="background:linear-gradient(135deg,#5a2a2a,#b04040)"></span>
      <span role="img" aria-label="Singer under stage lights" style="background:linear-gradient(135deg,#1a1a3a,#5a4a7a)"></span>
      <span role="img" aria-label="Performer in sequin outfit" style="background:linear-gradient(135deg,#8a1a2a,#c08a3a)"></span>
      <span role="img" aria-label="Band on a lit stage" style="background:linear-gradient(135deg,#3a4ab0,#a04ab0)"></span>
      <span role="img" aria-label="Concert stage with blue lights" style="background:linear-gradient(135deg,#6aa0e0,#b0c0f0)"></span>
    </div>
    <div class="arrows">‹ ›</div>
  </section>

  <section class="abs panel box social-box">
    <div class="box-head">Circlebook</div>
    <div class="page">Ember Velvet Hall</div>
    <div class="fans">
      <span role="img" aria-label="Guest photo" style="background:linear-gradient(135deg,#3a4a8a,#c0c0d0)"></span>
      <span role="img" aria-label="Guest photo" style="background:linear-gradient(135deg,#2a3a7a,#8a9ac0)"></span>
      <span role="img" aria-label="Guest photo" style="background:linear-gradient(135deg,#4a3a6a,#b0a0b0)"></span>
      <span role="img" aria-label="Guest photo" style="background:linear-gradient(135deg,#3a4a8a,#c0b0b0)"></span>
      <span role="img" aria-label="Guest photo" style="background:linear-gradient(135deg,#d0d0d0,#6a5a4a)"></span>
      <span role="img" aria-label="Guest photo" style="background:linear-gradient(135deg,#3a4ab0,#d0c0c0)"></span>
      <span role="img" aria-label="Guest photo" style="background:linear-gradient(135deg,#4a5aa0,#c0b0a0)"></span>
      <span role="img" aria-label="Guest photo" style="background:linear-gradient(135deg,#1a2a5a,#d0d0d0)"></span>
    </div>
    <div class="like"></div>
    <div class="like-info">18, 8654 People Likes<br>Ember Velvet Hall</div>
  </section>

  <section class="abs panel box booking">
    <div class="box-head"><span>Online&nbsp;<em>Booking</em></span></div>
    <div class="item" style="top:65px">
      <div class="pic" role="img" aria-label="Crowd dancing under colourful lights" style="background:linear-gradient(135deg,#e0a030,#3a6ad0)"></div>
      <div class="name">Quam libero eu montes</div>
      <div class="price">$ 250.45</div>
      <div class="info">Info</div><div class="buy">Buy Now</div>
    </div>
    <div class="item" style="top:178px">
      <div class="pic" role="img" aria-label="DJ with headphones under red light" style="background:linear-gradient(135deg,#e03020,#601010)"></div>
      <div class="name">Quam libero eu montes</div>
      <div class="price">$ 250.45</div>
      <div class="info">Info</div><div class="buy">Buy Now</div>
    </div>
  </section>

  <section class="abs panel box signup">
    <h2>Email <em>Signup</em></h2>
    <div class="field" style="top:56px">Name</div>
    <div class="field" style="top:98px">Email</div>
    <div class="field" style="top:140px;height:55px">Comment</div>
    <div class="poster" role="img" aria-label="Event poster for DJ Kairo electro night" style="background:linear-gradient(135deg,#2a3a44,#5a6670 60%,#1a2228)"></div>
    <div class="btn-sign">Sing Up</div>
  </section>

  <footer class="abs footer">
    <nav><span>Home</span><i>|</i><span>Photo</span><i>|</i><span>Weekly Specials</span><i>|</i><span>Events</span><i>|</i><span>Booking</span><i>|</i><span>Contact us</span></nav>
    <div class="legal">Copyright © Ember Velvet Hall 2011 All Rights Reserved.<br>Powered by Upward Studio</div>
    <div class="pay"><small>Secure Payments By</small><b>SwiftPay</b>
      <div class="cards"><span></span><span></span><span></span><span></span></div>
    </div>
  </footer>
</body>
</html>
```